Simple, High-Class Web Design Wanted - Motivational Speakers Site

1. Full Brief/Request & Specs outlined on following video -
http://clipvane-recorder.com/watch/tbWrkLmQyP

2. Use colours, images as you feel suits objective (we are happy to pay up to US$30 for any good images but must have licence/permission).

3. Layout probably similar to existing site - www.podiumvoicehub.com.au / http://podiumvoicehub.com.au/contact.php

4. Must Be Able to Coded for MOBILE-FRIENDLINESS & WordPress friendly Ideal.

5. This is the first, small job of many we/graphic design jobs. If suits, winning designer may be offered all future work direct.

Thanks & look forward to your design. Glen.

Target Market(s)

corporates - high end

Number of Pages Required

2 page

Font styles to use
Sans Serif

Requirements
Must have
• Classy professional look
Nice to have
• all in Video in brief
Should not have
• too many images / new images I haven't approved

```html
<!DOCTYPE html>
<html lang="en">
<head>
<meta charset="utf-8">
<title>Podium Voice Hub – Find the Perfect Speaker</title>
<link href="https://fonts.googleapis.com/css2?family=Open+Sans:ital,wght@0,400;0,600;0,700;1,400;1,600&display=swap" rel="stylesheet">
<style>
:root{
  --navy:#1b2b47;
  --navy-deep:#121e33;
  --orange:#e5511c;
  --orange-dark:#c9410f;
  --sky:#dbe8f3;
  --sky-soft:#eef4f9;
  --ink:#333a44;
  --blue-text:#2d5f93;
  --white:#ffffff;
}
*{box-sizing:border-box;margin:0;padding:0}
html,body{width:814px;height:1200px;overflow:hidden;background:var(--white)}
body{font-family:"Open Sans",Arial,sans-serif;color:var(--ink)}
.page{position:relative;width:814px;height:1200px;overflow:hidden}

/* header */
.site-header{height:52px;background:var(--navy);display:flex;align-items:center;justify-content:space-between;padding:0 24px}
.site-title{color:var(--white);font-size:17px;font-weight:600;line-height:1.15}
.site-title em{display:block;color:var(--orange);font-size:12px;font-weight:600}
.header-actions{display:flex;gap:10px}
.outline-btn{display:flex;align-items:center;gap:6px;border:1px solid rgba(255,255,255,.7);color:var(--white);font-size:11px;font-weight:600;padding:6px 12px;border-radius:2px}
.outline-btn svg{width:13px;height:13px}

/* hero */
.hero{position:relative;height:350px;background:linear-gradient(90deg,#f4f7fa 0%,#e9eff5 45%,#cfdbe6 100%);overflow:hidden}
.hero-photo{position:absolute;right:0;top:0;width:440px;height:350px;background:radial-gradient(ellipse at 62% 35%,#c3ccd6 0%,#a9b6c4 35%,rgba(200,212,224,0) 70%),linear-gradient(180deg,rgba(233,239,245,0) 60%,#8d98a6 100%)}
.hero-audience{position:absolute;left:0;bottom:0;width:100%;height:90px;background:linear-gradient(180deg,rgba(240,244,248,0),#7f8a97)}
.hero-copy{position:absolute;left:26px;top:40px;width:330px}
.hero-copy h1{font-size:25px;font-weight:400;color:var(--blue-text);line-height:1.3}
.hero-copy h1 strong{font-weight:700}
.solid-btn{display:inline-block;background:var(--orange);color:var(--white);font-size:11px;font-weight:700;padding:8px 14px;border-radius:2px;text-transform:uppercase}
.hero-copy .solid-btn{margin-top:22px}

/* intro */
.intro{display:flex;gap:22px;padding:20px 26px 0;height:228px}
.intro-text{width:390px;font-size:11px;line-height:1.5}
.intro-text p{margin-bottom:9px}
.intro-text .eg{font-weight:700;display:flex;align-items:center;gap:6px}
.video{width:350px}
.video-frame{height:168px;border:4px solid #e3e6ea;background:linear-gradient(180deg,#d9dde2,#aeb6bf)}
.video-bar{height:16px;background:#2b2f36;margin-top:-20px;position:relative;margin-left:4px;margin-right:4px}
.video .solid-btn{display:block;text-align:center;margin-top:10px}

/* criteria */
.criteria{display:flex;gap:10px;padding:0 26px;height:112px}
.criterion{flex:1;background:var(--sky);text-align:center;padding:10px 8px}
.criterion svg{width:30px;height:30px}
.criterion h3{font-size:11px;font-weight:700;color:var(--navy);margin-top:4px}
.criterion p{font-size:10px;line-height:1.35;margin-top:3px}

.closing{padding:14px 26px 0;font-size:11px;line-height:1.5;height:62px}

/* contact row */
.contact-row{display:flex;align-items:center;gap:14px;padding:0 26px;height:56px;border-top:1px solid #e1e5ea;border-bottom:1px solid #e1e5ea;margin:0 26px;padding:0}
.contact-row .solid-btn{padding:10px 40px;font-size:12px}
.spacer{flex:1}
.ghost-btn{display:flex;align-items:center;gap:6px;border:1px solid var(--blue-text);color:var(--blue-text);font-size:12px;font-weight:600;padding:8px 14px;border-radius:2px}
.ghost-btn svg{width:14px;height:14px}

/* note */
.note{margin-top:18px;background:var(--sky-soft);padding:18px 26px;height:226px}
.note h2{font-size:13px;font-weight:700;color:var(--navy);margin-bottom:10px}
.note ul{list-style:none;font-size:11px;line-height:1.55}
.note li{position:relative;padding-left:12px;margin-bottom:10px}
.note li::before{content:"";position:absolute;left:0;top:7px;width:4px;height:4px;background:var(--ink)}

/* footer */
.site-footer{position:absolute;left:0;bottom:0;width:100%;height:98px;background:var(--navy-deep);color:#c4ccd8;font-size:9.5px;text-align:center;padding-top:34px;line-height:1.6}
</style>
</head>
<body>
<div class="page">
  <header class="site-header">
    <div class="site-title">Find the Perfect Speaker for Your Next Event Here...<em>Free Industry Service</em></div>
    <div class="header-actions">
      <span class="outline-btn"><svg viewBox="0 0 16 16" fill="none" stroke="#fff" stroke-width="1.4"><rect x="1.5" y="3.5" width="13" height="9"/><path d="M1.5 3.5l6.5 5 6.5-5"/></svg>EMAIL US</span>
      <span class="outline-btn"><svg viewBox="0 0 16 16" fill="#fff"><path d="M4 1.5l2.5 3-1.5 1.5c.8 2 2.3 3.5 4.5 4.5L11 9l3 2.5-1.5 2.5C7 13.5 2.5 9 2 3z"/></svg>1300 48 27 19</span>
    </div>
  </header>

  <section class="hero">
    <div class="hero-photo" role="img" aria-label="Presenter in a suit speaking into a microphone on stage"></div>
    <div class="hero-audience" role="img" aria-label="Audience seated in a conference hall, seen from behind"></div>
    <div class="hero-copy">
      <h1>Looking for a top <strong>motivational</strong> a guest speaker,<br><br>MC, A Industry expert to <strong>“WOW”</strong> your next event?</h1>
      <span class="solid-btn">Find them here</span>
    </div>
  </section>

  <section class="intro">
    <div class="intro-text">
      <p>Podium Voice Hub is a <strong>free industry service</strong> designed to help people looking for speakers save precious time and frustration in finding the most suitable/best speaker for their needs.</p>
      <p>Suggestions are given by Australian conference speaker Glen Harlow, who has presided around Australia for a number of years and is familiar with many of our top professional speakers, MC’s as well as the leading speaker bureaus.</p>
      <p>If you would like a hand finding some good speaker options, simply send us the details of your event and the type of presenter you are ideally after,</p>
      <p class="eg">e.g. <svg width="60" height="10" viewBox="0 0 60 10"><path d="M0 5h54M50 1l5 4-5 4" stroke="#333a44" stroke-width="1.4" fill="none"/></svg></p>
    </div>
    <div class="video">
      <div class="video-frame" role="img" aria-label="Video of the speaker introducing the service"></div>
      <div class="video-bar"></div>
      <span class="solid-btn">I want to make our event a great success</span>
    </div>
  </section>

  <section class="criteria">
    <div class="criterion">
      <svg viewBox="0 0 30 30"><circle cx="15" cy="15" r="15" fill="#2d5f93"/><circle cx="15" cy="11" r="4" fill="#fff"/><path d="M8 23c0-4 3-6 7-6s7 2 7 6z" fill="#fff"/></svg>
      <h3>TYPE/STYLE</h3><p>Motivational, Entertaining, Keynote/Workshop, MC etc</p>
    </div>
    <div class="criterion">
      <svg viewBox="0 0 30 30"><circle cx="15" cy="15" r="15" fill="#2d5f93"/><rect x="9" y="7" width="12" height="16" fill="#fff"/><path d="M11 11h8M11 14h8M11 17h6" stroke="#2d5f93" stroke-width="1.2"/></svg>
      <h3>TOPIC/AREA</h3><p>Team Building, Leadership, Inspiration, Health/Life Balance etc</p>
    </div>
    <div class="criterion">
      <svg viewBox="0 0 30 30"><circle cx="15" cy="15" r="15" fill="#2d5f93"/><text x="15" y="21" text-anchor="middle" font-family="Open Sans, sans-serif" font-weight="700" font-size="16" fill="#fff">$</text></svg>
      <h3>APPROXIMATE BUDGET</h3><p>$1000, $2500, $5000, $7500+ etc</p>
    </div>
    <div class="criterion">
      <svg viewBox="0 0 30 30"><circle cx="15" cy="15" r="15" fill="#2d5f93"/><path d="M15 6a6 6 0 0 0-6 6c0 4.5 6 11 6 11s6-6.5 6-11a6 6 0 0 0-6-6z" fill="#fff"/><circle cx="15" cy="12" r="2.2" fill="#2d5f93"/></svg>
      <h3>LOCATION</h3><p>Sydney, Melbourne, Brisbane, Perth, Adelaide, Canberra etc</p>
    </div>
  </section>

  <p class="closing">and where we can, we will be happy to send you some speaker possibilities/ideas, trusted speakers bureaus or simply some thoughts on the best places for you to look. Regards Glen.</p>

  <div class="contact-row">
    <span class="solid-btn">Quick online contact form ▸</span>
    <span class="spacer"></span>
    <span class="ghost-btn"><svg viewBox="0 0 16 16" fill="none" stroke="#2d5f93" stroke-width="1.4"><rect x="1.5" y="3.5" width="13" height="9"/><path d="M1.5 3.5l6.5 5 6.5-5"/></svg>EMAIL US</span>
    <span class="ghost-btn"><svg viewBox="0 0 16 16" fill="#2d5f93"><path d="M4 1.5l2.5 3-1.5 1.5c.8 2 2.3 3.5 4.5 4.5L11 9l3 2.5-1.5 2.5C7 13.5 2.5 9 2 3z"/></svg>1300 48 27 19</span>
  </div>

  <section class="note">
    <h2>Please Note:</h2>
    <ul>
      <li>Any information you provide will ONLY ever be used to help with your specific enquiry.</li>
      <li>Glen does not have any financial agreements with any individual speakers he recommends. He offers this service, as it only takes a few minutes of his time, helps promote other professional speakers and obviously keeps his own name out there in the industry.</li>
      <li>Please understand that while Glen tries to respond quickly, due to his own speaking/travel commitments it may take up to 24 hours.</li>
    </ul>
  </section>

  <footer class="site-footer">
    © 2015. All Rights Reserved www.podiumvoicehub.com.au PO Box 412 Coralbay NSW 2099<br>
    E-mail: hello@podiumvoicehub.com.au Phone: 1300 48 27 19
  </footer>
</div>
</body>
</html>
```